Manufacturing Company Business card

K & T is a leading supplier of complex machine parts, assemblies and sub assemblies to the aerospace industry.
we would like to create a new feel for our manufacturing company business card design.
We are into lean manufacturing, bold design, metal, use current logo, use "this is your life" logo for entire back of card. updated look for 2015, text, bardcode, etc

our primary end use is flight control components used on about all commercial and business jets in use as well as military aircraft and civil aviation.

Reason: Need more time to review with internal team at KTmfg:)

Target Market(s)

aerospace, manufacturing

Industry/Entity Type

Aero

Contact Information for Business Card

New, industrial, trendy, use current logo, we like text, vmail is lame :( cell ph is ok - what is a fax???

Font styles to use
Serif
Sans Serif

Requirements
Must have
• incorporate our current logo, one option is an Industrial look, metal etc. we can also try to incorporate the feel of the back of the card onto the front but not so busy.
• Back of card full size "this is your life"
• front side, barcode, cell, - our motto "solutions in manufacturing" tm
Nice to have
• Professional look
• up to date
• appeals to broad audience
Should not have
• too much content - pictures of planes

```html
<!DOCTYPE html>
<html lang="en">
<head>
<meta charset="utf-8">
<title>K &amp; T Manufacturing – Business Card</title>
<link href="https://fonts.googleapis.com/css2?family=Open+Sans:wght@400;600;700&display=swap" rel="stylesheet">
<style>
  :root {
    --backdrop: #4a4d56;
    --card-white: #ffffff;
    --brand-green: #14a05a;
    --brand-gold: #bcac78;
    --ink-dark: #231f20;
    --ink-light: #ffffff;
    --ring-grey: #cfcfcf;
  }
  html, body {
    margin: 0;
    width: 1200px;
    height: 900px;
    overflow: hidden;
    background: var(--backdrop);
    font-family: "Open Sans", Arial, sans-serif;
  }
  .card-pair {
    position: absolute;
    inset: 0;
    display: flex;
    align-items: center;
    justify-content: center;
    gap: 40px;
  }
  .card {
    position: relative;
    width: 540px;
    height: 309px;
    background: var(--card-white);
    overflow: hidden;
    box-shadow: 0 6px 18px rgba(0,0,0,0.35);
  }
  .card-shapes {
    position: absolute;
    inset: 0;
    width: 100%;
    height: 100%;
  }
  .shape-green { fill: var(--brand-green); }
  .shape-gold { fill: var(--brand-gold); }

  .brand {
    position: absolute;
    display: flex;
    align-items: center;
    gap: 10px;
  }
  .brand-dot {
    width: 30px;
    height: 30px;
    border-radius: 50%;
    border: 2px solid var(--ring-grey);
    box-sizing: border-box;
  }
  .brand-name {
    font-weight: 700;
    font-size: 17px;
    letter-spacing: 1px;
    color: var(--ink-dark);
    text-transform: uppercase;
    white-space: nowrap;
  }
  .card-back .brand { left: 160px; top: 70px; }
  .card-front .brand { left: 44px; top: 112px; }

  .contact {
    position: absolute;
    right: 22px;
    top: 110px;
    text-align: right;
    color: var(--ink-light);
  }
  .contact-name {
    margin: 0;
    font-size: 20px;
    font-weight: 600;
    line-height: 1.1;
    white-space: nowrap;
  }
  .contact-role {
    margin: 0 0 6px;
    font-size: 12px;
    color: var(--ink-dark);
  }
  .contact-lines {
    list-style: none;
    margin: 0;
    padding: 0;
    font-size: 12px;
    line-height: 1.45;
  }
  .contact-lines li {
    display: flex;
    justify-content: flex-end;
    align-items: center;
    gap: 6px;
    white-space: nowrap;
  }
  .contact-icon {
    width: 10px;
    height: 10px;
    fill: none;
    stroke: var(--ink-dark);
    stroke-width: 1.4;
  }
</style>
</head>
<body>
<main class="card-pair">

  <section class="card card-back" aria-label="Card back">
    <svg class="card-shapes" viewBox="0 0 540 309" preserveAspectRatio="none" aria-hidden="true">
      <path class="shape-gold" d="M0,176 Q270,214 540,62 L540,309 L0,309 Z"/>
      <path class="shape-green" d="M0,192 Q275,228 540,84 L540,309 L0,309 Z"/>
    </svg>
    <div class="brand">
      <span class="brand-dot"></span>
      <span class="brand-name">K &amp; T Manufacturing</span>
    </div>
  </section>

  <section class="card card-front" aria-label="Card front">
    <svg class="card-shapes" viewBox="0 0 540 309" preserveAspectRatio="none" aria-hidden="true">
      <path class="shape-green" d="M448,0 Q360,170 0,264 L0,309 L540,309 L540,0 Z"/>
      <path class="shape-gold" d="M470,0 Q380,180 0,272 L0,309 L540,309 L540,0 Z"/>
    </svg>
    <div class="brand">
      <span class="brand-dot"></span>
      <span class="brand-name">K &amp; T Manufacturing</span>
    </div>
    <div class="contact">
      <p class="contact-name">Alan Mercer</p>
      <p class="contact-role">Owner</p>
      <ul class="contact-lines">
        <li>+33 210 555 014
          <svg class="contact-icon" viewBox="0 0 10 10" aria-label="Mobile"><rect x="2.5" y="0.8" width="5" height="8.4" rx="1"/></svg>
        </li>
        <li>+33-2100-5550
          <svg class="contact-icon" viewBox="0 0 10 10" aria-label="Phone"><path d="M2 1 L4 1 L4.5 3 L3.3 4 Q4.5 6 6 6.7 L7 5.5 L9 6 L9 8 Q5 9 1 3 Z"/></svg>
        </li>
        <li>+33 2105 5501
          <svg class="contact-icon" viewBox="0 0 10 10" aria-label="Fax"><rect x="1" y="4" width="8" height="4"/><rect x="3" y="1" width="4" height="3"/></svg>
        </li>
      </ul>
    </div>
  </section>

</main>
</body>
</html>
```